iOS developer portal page

We need a web design for a company based in Beijing called BrivoKids. Our company develops an SDK used by iOS developers making children's educational apps. The SDK provides cross-promotional marketing, user analytics, teacher feedback and activities, and parent reports for developers who implement it.
Our company offers a product that benefits parents and developers, however the design we need is in regard to the landing page for developers using our product.Developers using our SDK are mostly based in the USA and develop apps for the USA Pexora Tunebay store.
There is an included wireframe for the first design idea. Design comps can be similar or different from the wireframe, however it should be considered as a good starting point for the final design.
Updates
Thank you for the design submissions. We are currently reviewing the designs internally and will notify all designers once a decision has been reached.
Kind regards,
Gerrit
Reason: The deadline is being extended by one day so it will be closed at the end of the business week. Thank you.
Target Market(s)
iOS Developers for Children's education apps
Industry/Entity Type
It Company
Look and feel
Each slider illustrates characteristics of the customer's brand and the style your logo design should communicate.

```html
<!DOCTYPE html>
<html lang="en">
<head>
<meta charset="utf-8">
<title>BrivoKids – Developer Portal</title>
<link rel="stylesheet" href="https://fonts.googleapis.com/css2?family=Source+Sans+3:wght@400;600;700&family=Open+Sans:wght@400;600;700&family=Fredoka:wght@600&display=swap">
<style>
:root{
  --bg-top:#f7fbd8;
  --bg-mid:#a6d84a;
  --bg-bottom:#46a612;
  --nav-dark:#0b5a9c;
  --nav-light:#2c8fd4;
  --banner-red:#e3063d;
  --panel:#ffffff;
  --ink:#111111;
  --body-ink:#333333;
  --green-text:#3d9a0c;
  --testimonial-blue:#2d87c8;
  --logo-green:#6cbf1a;
  --rule:#d6d6d6;
}
*{box-sizing:border-box;margin:0;padding:0}
html,body{width:900px;height:1200px;overflow:hidden}
body{
  position:relative;
  font-family:"Source Sans 3",Arial,sans-serif;
  color:var(--ink);
  background:linear-gradient(to bottom,var(--bg-top) 0,#e4f3a6 200px,var(--bg-mid) 620px,#6dbd22 900px,var(--bg-bottom) 1200px);
}
.abs{position:absolute}
.brand{left:145px;top:36px;display:flex;align-items:center;gap:8px}
.brand-mark{width:22px;height:22px;border-radius:50%;background:var(--logo-green)}
.brand-name{font-family:"Source Sans 3",sans-serif;font-weight:700;font-size:34px;color:var(--logo-green);letter-spacing:.5px}
.login{left:722px;top:82px;font-size:13px;color:#333;letter-spacing:.5px}

.nav{left:112px;top:104px;width:675px;height:28px;border-radius:14px;
  background:linear-gradient(to bottom,var(--nav-light),var(--nav-dark));display:flex;align-items:center;overflow:hidden}
.nav-home{width:46px;height:28px;display:flex;align-items:center;justify-content:center;border-right:1px solid #0a4b82}
.nav a{display:block;height:28px;line-height:28px;padding:0 13px;font-family:"Open Sans",sans-serif;font-weight:700;font-size:9.5px;color:#fff;text-decoration:none;border-right:1px solid #0a4b82}
.search{position:absolute;right:10px;top:5px;width:140px;height:18px;border-radius:9px;background:#fff;box-shadow:inset 0 1px 2px rgba(0,0,0,.35)}
.search svg{position:absolute;right:6px;top:3px}

.panel{background:var(--panel);border-radius:8px;left:112px;width:675px}

.hero{top:147px;height:195px}
.hero-inner{position:absolute;left:8px;top:7px;width:660px;height:180px;border-radius:5px;background:var(--banner-red);overflow:hidden}
.hero-photo{position:absolute;left:0;top:0;width:225px;height:180px;background:linear-gradient(135deg,#e9e1d3,#c9b59a 55%,#8c7c6a);border-top-right-radius:0}
.hero-curve{position:absolute;left:190px;top:0}
.hero h1{position:absolute;left:228px;top:22px;font-weight:400;font-size:22px;line-height:24px;color:#fff}
.hero p{position:absolute;left:226px;top:76px;width:424px;font-size:12.6px;line-height:14.4px;color:#fff}
.dots{position:absolute;right:14px;bottom:6px;display:flex;gap:4px}
.dots span{width:7px;height:7px;border-radius:50%;background:#f58aa2}
.dots span.on{background:#fff}

.section-title{left:137px;top:358px;font-size:24px;font-weight:400}

.features{top:388px;height:232px}
.feature{position:absolute;top:0}
.feature h3{font-weight:400;font-size:13.5px;line-height:16px}
.feature .art{margin-top:6px;width:70px;height:62px;border-radius:6px}
.feature p{font-family:"Open Sans",Verdana,sans-serif;font-size:8.4px;line-height:12px;color:var(--body-ink);width:154px}
.read-more{position:absolute;width:80px;height:16px;border-radius:8px;border:1px solid #bbb;background:linear-gradient(#fff,#ececec);font-family:"Open Sans",sans-serif;font-size:7.5px;color:#555;letter-spacing:.5px;line-height:14px;padding-left:9px}
.read-more::after{content:"";position:absolute;right:0;top:0;width:15px;height:14px;border-left:1px solid #ccc}
.read-more i{position:absolute;right:4px;top:4px;width:0;height:0;border-left:5px solid var(--green-text);border-top:3px solid transparent;border-bottom:3px solid transparent}

.spotlight{top:631px;height:222px}
.spot-title{left:17px;top:28px;font-size:16px}
.app-icon{border-radius:4px}
.app-meta{font-size:11px;line-height:13.5px}
.app-meta .enabled{color:var(--green-text);font-size:12px}
.small{font-size:8.5px;color:#333}
.store-badge{width:57px;height:22px;border-radius:4px;background:linear-gradient(#7a7a7a,#3a3a3a)}
.testimonials{left:488px;top:32px;width:146px;border-bottom:1px solid var(--rule);padding-bottom:3px;color:var(--testimonial-blue);font-size:16px}
.quote{left:484px;top:144px;width:160px;font-family:"Open Sans",sans-serif;font-size:8.5px;line-height:10.5px;color:#333}
.quote-by{left:534px;top:193px;font-family:"Open Sans",sans-serif;font-weight:700;font-size:8.5px;color:#333}

.recent{top:865px;height:238px}
.recent-title{left:17px;top:12px;font-size:15px}

.footer-social{left:137px;top:1116px;display:flex;gap:6px}
.footer-social span{width:17px;height:17px;border-radius:2px}
.copyright{left:498px;top:1119px;font-family:Arial,sans-serif;font-size:10px;color:#111}
</style>
</head>
<body>
  <div class="abs brand"><span class="brand-mark"></span><span class="brand-name">BrivoKids</span></div>
  <div class="abs login">LOGIN</div>

  <nav class="abs nav">
    <div class="nav-home">
      <svg width="12" height="11" viewBox="0 0 12 11"><path d="M6 0L0 5h1.6v6h3.2V7.5h2.4V11h3.2V5H12z" fill="#fff"/></svg>
    </div>
    <a href="#">About</a><a href="#">News</a><a href="#">Support</a><a href="#">Contact</a>
    <div class="search"><svg width="11" height="11" viewBox="0 0 11 11"><circle cx="4.5" cy="4.5" r="3.5" fill="none" stroke="#666" stroke-width="1.4"/><path d="M7 7l3.5 3.5" stroke="#666" stroke-width="1.6"/></svg></div>
  </nav>

  <section class="abs panel hero">
    <div class="hero-inner">
      <div class="hero-photo" role="img" aria-label="Photo of two children smiling while using a tablet"></div>
      <svg class="hero-curve" width="60" height="180" viewBox="0 0 60 180"><path d="M24 0 Q-6 90 24 180 L60 180 L60 0 Z" fill="#e3063d"/><path d="M24 0 Q-6 90 24 180" fill="none" stroke="#fff" stroke-width="3"/></svg>
      <h1>Make Your Apps<br>IRRESISTABLE</h1>
      <p>Simply download and integrate our BrivoKids Software Developer Kit and you will suddenly plug into a world of invaluable feedback, usage data, cross-promotional opportunities and marketing support.&nbsp; The SDK adds less than 1 Mb to your app and integrates with just one line of code.</p>
      <div class="dots"><span></span><span></span><span class="on"></span><span></span></div>
    </div>
  </section>

  <h2 class="abs section-title">Enable These Great Features in Minutes!</h2>

  <section class="abs panel features">
    <div class="feature" style="left:12px;top:17px">
      <h3>Parent Report</h3>
      <div class="art" role="img" aria-label="Illustration of a checklist clipboard with a pie chart" style="background:linear-gradient(135deg,#e8dcc4,#6fb4e0)"></div>
      <p style="margin-top:10px">Lorem ipsum dolor sit amet, consectetur adi piscing elit. Donec consectetur, nibh ut feugiat placerat, orci lacus accumsan erat, eget porttitor arcu velit a lacus. Sed tempus bibendum risus.</p>
    </div>
    <div class="feature" style="left:193px;top:16px">
      <h3>Cross-promotional<br>Marketing</h3>
      <div class="art" role="img" aria-label="Illustration of glossy 3D bar chart with rising arrow" style="margin-left:20px;background:linear-gradient(135deg,#f0c040,#d83020)"></div>
      <p style="margin-top:7px">Lorem ipsum dolor sit amet, consectetur adi piscing elit. Donec consectetur, nibh ut feugiat placerat, orci lacus accumsan erat, eget porttitor arcu velit a lacus. Sed tempus bibendum risus.</p>
    </div>
    <div class="feature" style="left:367px;top:14px">
      <h3>Teacher Feedback &amp;<br>Activities</h3>
      <div class="art" role="img" aria-label="Illustration of a teacher writing on a whiteboard" style="margin-left:58px;background:linear-gradient(135deg,#e6eef4,#3b8fc8)"></div>
      <p style="margin-top:4px">Lorem ipsum dolor sit amet, consectetur adi piscing elit. Donec consectetur, nibh ut feugiat placerat, orci lacus accumsan erat, eget porttitor arcu velit a lacus. Sed tempus bibendum risus.</p>
    </div>
    <div class="feature" style="left:519px;top:9px">
      <h3>User Analytics</h3>
      <svg style="margin:8px 0 0 12px;display:block" width="70" height="58" viewBox="0 0 70 58">
        <defs><linearGradient id="barGrad" x1="0" y1="0" x2="0" y2="1"><stop offset="0" stop-color="#ffd21a"/><stop offset="1" stop-color="#f07a10"/></linearGradient></defs>
        <rect x="2" y="34" width="12" height="22" rx="3" fill="url(#barGrad)"/>
        <rect x="18" y="22" width="12" height="34" rx="3" fill="url(#barGrad)"/>
        <rect x="34" y="12" width="12" height="44" rx="3" fill="url(#barGrad)"/>
        <rect x="50" y="2" width="12" height="54" rx="3" fill="url(#barGrad)"/>
      </svg>
      <p style="margin-top:5px">Lorem ipsum dolor sit amet, consectetur adi piscing elit. Donec consectetur, nibh ut feugiat placerat, orci lacus accumsan erat, eget porttitor arcu velit a lacus. Sed tempus bibendum risus.</p>
    </div>
    <div class="read-more" style="left:30px;top:198px">Read More<i></i></div>
    <div class="read-more" style="left:246px;top:199px">Read More<i></i></div>
    <div class="read-more" style="left:408px;top:197px">Read More<i></i></div>
    <div class="read-more" style="left:576px;top:197px">Read More<i></i></div>
  </section>

  <section class="abs panel spotlight">
    <h3 class="abs spot-title" style="font-weight:400">Mira Knows Green: Water Conservation by TaleLark</h3>
    <div class="abs app-icon" role="img" aria-label="App artwork of a cartoon girl holding a leaf" style="left:19px;top:68px;width:86px;height:86px;background:linear-gradient(135deg,#f4d77a,#8cc6e8)"></div>
    <div class="abs app-meta" style="left:117px;top:67px"><div class="enabled">BrivoKids Reporting Enabled!</div>BrivoKids Summary:<br>Water Conservation - what can we do?</div>
    <div class="abs small" style="left:120px;top:163px">Age: 4 to 7</div>
    <div class="abs small" style="left:120px;top:184px">Subject: Language Science Learning Skills: Activity Types:</div>
    <div class="abs small" style="left:17px;top:182px;font-size:9px;color:#000">free</div>
    <div class="abs store-badge" style="left:35px;top:175px" role="img" aria-label="Pexora Tunebay store badge"></div>

    <div class="abs testimonials">Testimonials</div>
    <div class="abs" role="img" aria-label="Illustration of a notepad with pencil and a person" style="left:490px;top:60px;width:76px;height:76px;border-radius:6px;background:linear-gradient(135deg,#f2e2a0,#6aa8d8)"></div>
    <p class="abs quote">"I think the fact that you can get reports and stuff is great, I think that the schools ought to use this to track kids progress in school! It's very useful!"</p>
    <div class="abs quote-by">- Rosa, Mother of Two</div>
  </section>

  <section class="abs panel recent">
    <h3 class="abs recent-title" style="font-weight:400">Recent Releases</h3>
    <div class="abs app-icon" role="img" aria-label="App artwork of a cartoon caterpillar with letter blocks" style="left:19px;top:40px;width:86px;height:86px;border-radius:12px;background:linear-gradient(135deg,#7fd0f0,#8cd04a)"></div>
    <div class="abs app-meta" style="left:115px;top:45px"><div class="enabled">BrivoKids Reporting Enabled!</div>BrivoKids Summary:<br>Water Conservation - what can we do?</div>
    <div class="abs app-icon" role="img" aria-label="App artwork of cartoon fruit characters with numbers" style="left:332px;top:28px;width:86px;height:86px;background:linear-gradient(135deg,#5fb83a,#e8a030)"></div>
    <div class="abs app-meta" style="left:431px;top:40px"><div class="enabled">BrivoKids Reporting Enabled!</div>BrivoKids Summary:<br>Water Conservation - what can we do?</div>
    <div class="abs app-icon" role="img" aria-label="App artwork of a number keypad" style="left:21px;top:135px;width:86px;height:86px;background:linear-gradient(135deg,#3fa84a,#2a7a30)"></div>
    <div class="abs app-meta" style="left:115px;top:140px"><div class="enabled">BrivoKids Reporting Enabled!</div>BrivoKids Summary:<br>Water Conservation - what can we do?</div>
    <div class="abs app-icon" role="img" aria-label="App artwork of a cartoon girl holding a leaf" style="left:330px;top:129px;width:86px;height:86px;background:linear-gradient(135deg,#f4d77a,#8cc6e8)"></div>
    <div class="abs app-meta" style="left:431px;top:131px"><div class="enabled">BrivoKids Reporting Enabled!</div>BrivoKids Summary:<br>Water Conservation - what can we do?</div>
  </section>

  <footer>
    <div class="abs footer-social" aria-label="Social links">
      <span style="background:#8a8a8a"></span><span style="background:#3a6fc4"></span><span style="background:#1d7fc4"></span><span style="background:#f08a24"></span>
    </div>
    <div class="abs copyright">Copyright 2011 © BrivoKids All rights reserved.</div>
  </footer>
</body>
</html>
```